7 Elite Label

Design a label for 7 Elite styling gels. The logo is attached. The color is C=100, M=100, Y=0, K=0. The 16 oz. jar is also attached.

Updates

Attention all designers,

The old logo has been deleted.  I have uploaded a new logo for this project.  Can you please update your design with the NEW LOGO?
thank you,
Rob

Target Market(s)

Multicultural

Requirements
Must have
• you must used the logo attached.

text to be included on the jar:

Used by Professionals
Maximum Hold
Alcohol Free
NO FLAKING

16 oz.

As far as label size, use the jar photo, and fit the design on it.

```html
<!DOCTYPE html>
<html lang="en">
<head>
<meta charset="UTF-8">
<title>7 Elite Styling Gel Label</title>
<link rel="stylesheet" href="https://fonts.googleapis.com/css2?family=Fredoka:wght@500;600&family=Grandstander:wght@700&display=swap">
<style>
  :root {
    --ink-blue: #2e3192;
    --lavender: #aaa9d6;
    --lavender-deep: #8c8bcb;
    --label-white: #ffffff;
    --page: #f2f2f4;
    --size-mark: #f4f4f8;
  }
  html, body {
    margin: 0;
    padding: 0;
    width: 1032px;
    height: 1200px;
    overflow: hidden;
    background: var(--page);
  }
  .canvas {
    position: relative;
    width: 1032px;
    height: 1200px;
  }
  .label {
    position: absolute;
    left: 136px;
    top: 137px;
    width: 760px;
    height: 925px;
    background: var(--label-white);
    overflow: hidden;
    box-shadow: 0 2px 10px rgba(0,0,0,0.08);
  }
  .label-art {
    position: absolute;
    inset: 0;
    width: 100%;
    height: 100%;
  }
  .band { fill: var(--lavender); }
  .rule { fill: none; stroke: var(--ink-blue); stroke-width: 6; }

  .brand {
    position: absolute;
    left: 170px;
    width: 450px;
    top: 290px;
    display: flex;
    align-items: center;
    justify-content: center;
    gap: 20px;
  }
  .brand-dot {
    flex: none;
    width: 110px;
    height: 110px;
    border-radius: 50%;
    background: var(--ink-blue);
  }
  .brand-name {
    font-family: "Fredoka", sans-serif;
    font-weight: 600;
    font-size: 96px;
    line-height: 1;
    color: var(--ink-blue);
    white-space: nowrap;
  }
  .slogan {
    position: absolute;
    left: 40px;
    width: 700px;
    top: 478px;
    margin: 0;
    text-align: center;
    font-family: "Grandstander", cursive;
    font-weight: 700;
    font-size: 52px;
    line-height: 1.2;
    color: var(--lavender-deep);
    -webkit-text-stroke: 1.5px var(--ink-blue);
    letter-spacing: 1px;
    white-space: nowrap;
  }
  .claims {
    position: absolute;
    left: 60px;
    width: 620px;
    top: 582px;
    margin: 0;
    text-align: center;
    font-family: "Fredoka", sans-serif;
    font-weight: 500;
    font-size: 23px;
    line-height: 1.2;
    color: var(--ink-blue);
    letter-spacing: 0.3px;
    white-space: nowrap;
  }
  .net-weight {
    position: absolute;
    right: 18px;
    bottom: 48px;
    font-family: "Times New Roman", serif;
    font-size: 34px;
    color: var(--size-mark);
  }
</style>
</head>
<body>
<div class="canvas">
  <section class="label">
    <svg class="label-art" viewBox="0 0 575 700" preserveAspectRatio="none" aria-hidden="true">
      <path class="band band-top" d="M0,0 H575 V35 C480,95 330,110 200,102 C140,160 80,230 0,265 Z"/>
      <path class="rule rule-top" d="M0,274 C82,239 142,169 205,112 C332,120 482,107 575,47"/>
      <path class="rule rule-bottom" d="M0,600 C110,588 250,585 330,592 C395,528 485,468 575,450"/>
      <path class="band band-bottom" d="M0,612 C110,600 250,597 337,604 C402,540 490,480 575,462 V700 H0 Z"/>
    </svg>

    <div class="brand">
      <span class="brand-dot"></span>
      <span class="brand-name">7 Elite</span>
    </div>

    <p class="slogan">Used by Professionals</p>
    <p class="claims">MAXIMUM HOLD • ALCOHOL FREE • NO FLAKING</p>
    <span class="net-weight">16 oz</span>
  </section>
</div>
</body>
</html>
```